Metal Fabrication Business Cards

We need a business card for our business of Metal Fabrication/Welding. Our company is called "Hadley's Metal Fabrication"

We are a metal fabrication business which takes on "high class" clients- dealing with some of the biggest builders in Australia. Our work is neat, and the type of work we do is 2nd to none for quality. We want to show that on our cards. However, we would love to show a side that is down to earth and a bit more modern and contemporary - we are all young in business so would love to show that side - rather than a boring "very straight looking" card. We always have a clean workshop and take pride in our presentation. We want to come across like we are very rich, but would love to go for a surf as well! A card that basically says we have high class and will charge you a high rate - but the quality will be outstanding.

Front of card: - Simply but sharp!
-Thinking maybe white card - with nice black writing.
-On the right hand side of card a person welding - or holding a welder.
- My business name - Hadley's Metal Fabrication
-Also maybe my name - which is 'Corey" (if it doesn't work, we can put this on the back of card.)
- if needed to look better - we can put keywords on front of card like "metal fabrication, sheet metal, welding etc" but I dont want it to be crowded.

Back of card: - Also make smart but sharp!
Put details such as:
04387 21 914
hadley.fabrication@tinmailbox.com.au
7/32 Keel Street
South Lismore NSW 2480
www.korvinfabrication.com.au
ABN 72 615 803 914

thats just an idea - its now up to you. I don't mind what you come up with - as long as it stands out from the rest and looks sharp, professional but contemporary.

Business

Put details such as:
04387 21 914
7/32 Keel Street
South Lismore NSW 2480
ABN 72 615 803 914

Hadley's Metal Fabrication

```html
<!DOCTYPE html>
<html lang="en">
<head>
<meta charset="utf-8">
<title>Hadley's Metal Fabrication – Business Cards</title>
<link rel="stylesheet" href="https://fonts.googleapis.com/css2?family=Tinos:wght@400;700&display=swap">
<style>
  :root {
    --backdrop: #d2d2d2;
    --card: #ffffff;
    --gold: #c98a38;
    --ink: #141414;
  }
  * { margin: 0; padding: 0; box-sizing: border-box; }
  html, body {
    width: 1189px;
    height: 1200px;
    overflow: hidden;
    background: var(--backdrop);
    font-family: "Tinos", "Times New Roman", serif;
    color: var(--ink);
  }
  .card {
    position: absolute;
    left: 194px;
    width: 807px;
    height: 461px;
    background: var(--card);
  }
  .card--front { top: 111px; }
  .card--back { top: 619px; }

  .brand-name {
    position: absolute;
    left: 0;
    right: 0;
    text-align: center;
    font-weight: 700;
    font-size: 52px;
    color: var(--gold);
    white-space: nowrap;
  }
  .card--front .brand-name { top: 84px; }
  .card--back .brand-name { top: 112px; }

  .identity {
    position: absolute;
    right: calc(807px - 350px);
    top: 240px;
    text-align: right;
    white-space: nowrap;
  }
  .identity__name { font-size: 40px; line-height: 44px; }
  .identity__address { font-size: 20px; line-height: 23px; margin-top: 2px; }
  .identity__abn { font-size: 16px; line-height: 20px; margin-top: 5px; }

  .divider {
    position: absolute;
    left: 378px;
    top: 218px;
    width: 3px;
    height: 151px;
    background: var(--gold);
  }

  .contact-list {
    position: absolute;
    left: 408px;
    top: 252px;
    list-style: none;
  }
  .contact-list li {
    display: flex;
    align-items: center;
    height: 30px;
    font-size: 21px;
    white-space: nowrap;
  }
  .contact-list svg {
    width: 18px;
    height: 18px;
    margin-right: 13px;
    flex: none;
  }

  .services {
    position: absolute;
    left: 0;
    right: 0;
    top: 303px;
    text-align: center;
    font-size: 27px;
  }
</style>
</head>
<body>
  <section class="card card--front">
    <h1 class="brand-name">Hadley's Metal Fabrication</h1>

    <div class="identity">
      <p class="identity__name">Corey</p>
      <p class="identity__address">7/32 Keel Street South Lismore<br>NSW 2480</p>
      <p class="identity__abn">ABN 72 615 803 914</p>
    </div>

    <div class="divider"></div>

    <ul class="contact-list">
      <li>
        <svg viewBox="0 0 18 18" aria-hidden="true">
          <rect width="18" height="18" rx="2" fill="var(--gold)"/>
          <path d="M5 4 l2.5 0 l1 3 l-1.5 1 q1 2.5 3 3.5 l1 -1.5 l3 1 l0 2.5 q-7 0.5 -9 -9.5z" fill="#fff"/>
        </svg>
        04387 21 914
      </li>
      <li>
        <svg viewBox="0 0 18 18" aria-hidden="true">
          <rect width="18" height="18" rx="2" fill="var(--gold)"/>
          <rect x="3.5" y="5.5" width="11" height="7.5" fill="none" stroke="#fff" stroke-width="1.2"/>
          <path d="M3.5 5.5 L9 10 L14.5 5.5" fill="none" stroke="#fff" stroke-width="1.2"/>
        </svg>
        hadley.fabrication@tinmailbox.com.au
      </li>
      <li>
        <svg viewBox="0 0 18 18" aria-hidden="true">
          <rect width="18" height="18" rx="2" fill="var(--gold)"/>
          <circle cx="9" cy="9" r="5.5" fill="none" stroke="#fff" stroke-width="1.2"/>
          <ellipse cx="9" cy="9" rx="2.3" ry="5.5" fill="none" stroke="#fff" stroke-width="1"/>
          <line x1="3.5" y1="9" x2="14.5" y2="9" stroke="#fff" stroke-width="1"/>
        </svg>
        www.korvinfabrication.com.au
      </li>
    </ul>
  </section>

  <section class="card card--back">
    <h2 class="brand-name">Hadley's Metal Fabrication</h2>
    <p class="services">"metal fabrication, sheet metal, welding etc"</p>
  </section>
</body>
</html>
```